Fennick Grove Gummy Bottle Label Design

(see attached word doc for full project description and example labels we like)
PROJECT OVERVIEW:
Fennick Grove is a healthy blend of functional organic super mushroom gummies that aims to enhance mood and promote overall mental and physical well-being by taking daily doses. The gummy product line offers a range of benefits, including increased energy, focus, calmness, sleep, immunity defense and overall mood upliftment. Fennick Grove is a brand that exudes positivity, vitality and personal growth. Fennick Grove is accessible, friendly, and approachable, making it easy for customers to integrate the brand into their daily routine. We cater/celebrate self-care by tending to both mental health and physical health.

Each benefit (i.e. product & flavor) is assigned a specific color that represents that “mood.” There are a total of 6 Moods, all 6 colors must be cohesive together. We prefer the color that represents the Mood to also be a clear representation of the flavor assigned to that mood, but we are open to interpretation if the color story looks good. We are also open to imagery (either real images or flaticons representing the ingredients or flavors) on the labels to help illustrate the components of this delicious product.

LABEL REQUEST:
The Fennick Grove products are gummies that will be placed in bottles and bags. There will be 6 different products with designated moods and flavors (i.e. Sleep/Lavender Vanilla, Calm/blackberry, Uplift/Pineapple, Focus/peach, Defense/black cherry, Energy/orange).

Dimensions will vary, here are a few:
Bottles:
6" W x 2" H
5" W x 2" H

Pouches:
4 x 6 x 2"

PRODUCTS:

Uplifting
Flavor: Pineapple
Mood: Mood Enhancement, Mental Health Helper
Front Label Ingredients: Cordyceps
Back Label Ingredients: Magnesium, Vitamin B2, Theacrine, Rhodiola Rosea, Shiitake, Cordyceps, Myrcene, Pinene.

Focus
Flavor: Sunny Plume
Mood: Focused, Creative, Productive
Front Label Ingredients: Lion’s Mane & Cordyceps
Back Label Ingredients: Rhodiola Rosea, Theacrine, Luteolin, Forskolin, Lions Mane, Cordyceps, Caryphyllene, Linalool.

Defense
Flavor: Black Cherry
Mood: Immunity & Gut Health
Front Label Ingredients: Turkey Tail
Back Label Ingredients: Vit A, Vit C, Ginger, Magnesium Glycinate, Lemon Balm, Maitake, Turkey Tail, Humulene.

Energy
Flavor: Rocket Parade
Mood: Awake, Stamina, Active
Front Label Ingredients: Lions Mane & Cordyceps
Back Label Ingredients: (NALT) N-Acetylcysteine-L-Tyrosine NALT, Caffeine, Vitamin B1, B3, Rhodiola Rosea, Ginkgo, Cordyceps, Valencene, Lions Mane, Limonene.

Sleep
Flavor: Vanilla Lavender Marlow Tide blend
Mood: Bedtime, Naptime, Relax Time
Front Label Ingredients: Melatonin & Reishi
Back Label Ingredients: Melatonin, Ashwagandha, Reishi, Bobinsana, Passion Flower, Linalool.

Calm
Flavor: Juniper Reel
Mood: Chill, Relaxed, Good Vibes
Front Label Ingredients: Reishi & Ashwagandha
Back Label Ingredients: Ashwagandha, Lemon Balm, Reishi, Chamomile, Velvet Bean, Caryophyllene.

```html
<!DOCTYPE html>
<html lang="en">
<head>
<meta charset="utf-8">
<title>Fennick Grove Gummy Labels</title>
<link rel="stylesheet" href="https://fonts.googleapis.com/css2?family=Titan+One&family=Grenze+Gotisch:wght@700&display=swap">
<style>
:root{
  --board:#7b7b7b;
  --strip:#ffffff;
  --navy:#1e2a78;
  --orange:#f26a2e;
  --pink:#f0489a;
  --white:#ffffff;
  --brand:#f6c13b;
  --badge:#e9e9e9;
  --badge-edge:#555555;
}
*{margin:0;padding:0;box-sizing:border-box}
html,body{width:1200px;height:2400px;overflow:hidden;background:var(--board)}
.board{position:relative;width:1200px;height:2400px}

.label{position:absolute;overflow:hidden;box-shadow:0 14px 18px rgba(0,0,0,.35)}
.label--neon{left:72px;width:1056px;height:352px}
.label--psy{left:62px;width:1079px;height:358px}

/* per-mood colour stories */
.mood--calm{--m1:#5b2a9e;--m2:#2f7de0;--m3:#21c24d;--m4:#e0802a;--base:#0a1740}
.mood--sleep{--m1:#9b7ae6;--m2:#3fb0d8;--m3:#26c58a;--m4:#f0d9a8;--base:#121a4e}
.mood--energy{--m1:#ff7a1a;--m2:#2e63d8;--m3:#4fd22c;--m4:#ffc23a;--base:#0b1a3c}
.mood--defense{--m1:#6a0b2a;--m2:#b81238;--m3:#2a8a46;--m4:#2f6fc8;--base:#4a0820}
.mood--focus{--m1:#ff9e6e;--m2:#e2407e;--m3:#3aa85a;--m4:#ffd07a;--base:#8a1450}
.mood--uplift{--m1:#ffd21f;--m2:#d81e74;--m3:#49b83c;--m4:#ff9a2a;--base:#8e1046}

.artwork{position:absolute;left:0;top:0;right:0;bottom:24px}
.label--neon .artwork{background:
  radial-gradient(ellipse 90px 55px at 30% 20%,var(--m4) 0%,transparent 100%),
  radial-gradient(ellipse 80px 50px at 34% 58%,var(--m4) 0%,transparent 100%),
  radial-gradient(ellipse 60px 40px at 5% 78%,#ff6a1a 0%,transparent 100%),
  radial-gradient(ellipse 70px 45px at 72% 80%,#f3e06a 0%,transparent 100%),
  radial-gradient(ellipse 140px 90px at 20% 45%,var(--m3) 0%,transparent 100%),
  radial-gradient(ellipse 110px 70px at 76% 20%,var(--m2) 0%,transparent 100%),
  radial-gradient(ellipse 110px 70px at 90% 22%,var(--m1) 0%,transparent 100%),
  radial-gradient(ellipse 130px 70px at 88% 68%,var(--m2) 0%,transparent 100%),
  radial-gradient(ellipse 200px 160px at 58% 40%,var(--m1) 0%,transparent 100%),
  linear-gradient(135deg,var(--base),#06102a 50%,var(--base))}
.label--psy .artwork{background:
  radial-gradient(ellipse 110px 80px at 14% 68%,var(--m4) 0%,transparent 100%),
  radial-gradient(ellipse 90px 60px at 8% 88%,var(--m1) 0%,transparent 100%),
  radial-gradient(ellipse 120px 70px at 38% 20%,var(--m2) 0%,transparent 100%),
  radial-gradient(ellipse 150px 80px at 78% 22%,var(--m1) 0%,transparent 100%),
  radial-gradient(ellipse 90px 60px at 84% 56%,var(--m4) 0%,transparent 100%),
  radial-gradient(ellipse 120px 90px at 28% 48%,var(--m3) 0%,transparent 100%),
  radial-gradient(ellipse 140px 100px at 94% 80%,var(--m2) 0%,transparent 100%),
  radial-gradient(ellipse 140px 90px at 60% 78%,var(--m3) 0%,transparent 100%),
  linear-gradient(120deg,var(--base),#5a0a34 50%,var(--base))}

.mood-copy{position:absolute;left:34px;top:40px;width:196px}
.mood-title{font-family:"Titan One",cursive;font-size:15px;line-height:1.1;color:var(--pink);text-align:center;-webkit-text-stroke:3px var(--white);paint-order:stroke fill}
.mood-ingredients{margin-top:12px;font-family:"Titan One",cursive;font-size:7px;line-height:1.65;color:var(--white);letter-spacing:.2px}

.center{position:absolute;left:330px;top:18px;width:420px;text-align:center}
.brand{font-family:"Titan One",cursive;font-size:40px;color:var(--brand);line-height:1;height:86px;display:flex;align-items:center;justify-content:center;-webkit-text-stroke:5px var(--white);paint-order:stroke fill}
.product{margin-top:10px;font-family:"Titan One",cursive;font-size:42px;line-height:1;color:var(--orange);-webkit-text-stroke:6px var(--white);paint-order:stroke fill;letter-spacing:1px}
.species{margin-top:8px;font-family:"Grenze Gotisch",serif;font-weight:700;font-size:38px;line-height:1;color:var(--navy);-webkit-text-stroke:5px var(--white);paint-order:stroke fill}
.mood-word{margin-top:8px;font-family:"Titan One",cursive;font-size:15px;line-height:1;color:var(--pink);-webkit-text-stroke:3px var(--white);paint-order:stroke fill}
.flavor{margin-top:8px;font-family:"Titan One",cursive;font-size:7.5px;color:var(--white)}
.front-ingredients{margin-top:5px;font-family:"Grenze Gotisch",serif;font-weight:700;font-size:11px;color:var(--white);-webkit-text-stroke:2px var(--navy);paint-order:stroke fill}

.badges{position:absolute;right:8px;top:96px;display:flex;flex-direction:column;gap:7px}
.badge{display:block;width:18px;height:18px;border-radius:50%;background:var(--badge);border:2px solid var(--badge-edge)}

.strip{position:absolute;left:0;right:0;bottom:0;height:24px;background:var(--strip);font-family:"Titan One",cursive;font-size:10px;line-height:24px;color:var(--navy);letter-spacing:.3px}
.strip span{position:absolute;top:0}
.strip .dose{left:324px}
.strip .count{left:502px}
.strip .weight{left:610px}
</style>
</head>
<body>
<main class="board">

  <section class="label label--neon mood--calm" style="top:29px">
    <div class="artwork" role="img" aria-label="Glowing neon mushroom forest in blackberry purple and green"></div>
    <div class="mood-copy"><div class="mood-title">CHILL, RELAXED,<br>GOOD VIBES</div><p class="mood-ingredients">ASHWAGANDHA, LEMON BALM, REISHI, CHAMOMILE, VELVET BEAN, CARYOPHYLLENE.</p></div>
    <div class="center"><div class="brand">Fennick Grove</div><div class="product">MUSHROOM<br>GUMMIES</div><div class="species">Amanita Muscaria</div><div class="mood-word">CALM</div><div class="flavor">JUNIPER REEL</div><div class="front-ingredients">Reishi &amp; Ashwagandha</div></div>
    <div class="badges"><i class="badge"></i><i class="badge"></i><i class="badge"></i><i class="badge"></i><i class="badge"></i><i class="badge"></i><i class="badge"></i></div>
    <div class="strip"><span class="dose">2500 MG PER GUMMY</span><span class="count">30 GUMMIES</span><span class="weight">NET WT. = 4.76 OZ/(135G)</span></div>
  </section>

  <section class="label label--neon mood--sleep" style="top:412px">
    <div class="artwork" role="img" aria-label="Glowing neon mushroom forest in lavender and teal"></div>
    <div class="mood-copy"><div class="mood-title">BEDTIME, NAPTIME,<br>RELAX TIME</div><p class="mood-ingredients">MELATONIN, ASHWAGANDHA, REISHI, BOBINSANA, PASSION FLOWER, LINALOOL.</p></div>
    <div class="center"><div class="brand">Fennick Grove</div><div class="product">MUSHROOM<br>GUMMIES</div><div class="species">Amanita Muscaria</div><div class="mood-word">SLEEP</div><div class="flavor">VANILLA LAVENDER MARLOW TIDE BLEND</div><div class="front-ingredients">Melatonin &amp; Reishi</div></div>
    <div class="badges"><i class="badge"></i><i class="badge"></i><i class="badge"></i><i class="badge"></i><i class="badge"></i><i class="badge"></i><i class="badge"></i></div>
    <div class="strip"><span class="dose">2500 MG PER GUMMY</span><span class="count">30 GUMMIES</span><span class="weight">NET WT. = 4.76 OZ/(135G)</span></div>
  </section>

  <section class="label label--neon mood--energy" style="top:799px">
    <div class="artwork" role="img" aria-label="Glowing neon mushroom forest in orange and green"></div>
    <div class="mood-copy"><div class="mood-title">AWAKE, STAMINA, ACTIVE</div><p class="mood-ingredients">(NALT) N-ACETYLCYSTEINE-L-TYROSINE NALT, CAFFEINE, VITAMIN B1, B3, RHODIOLA ROSEA, GINKGO, CORDYCEPS, VALENCENE, LIONS MANE, LIMONENE.</p></div>
    <div class="center"><div class="brand">Fennick Grove</div><div class="product">MUSHROOM<br>GUMMIES</div><div class="species">Amanita Muscaria</div><div class="mood-word">ENERGY</div><div class="flavor">ROCKET PARADE</div><div class="front-ingredients">Lions Mane &amp; Cordyceps</div></div>
    <div class="badges"><i class="badge"></i><i class="badge"></i><i class="badge"></i><i class="badge"></i><i class="badge"></i><i class="badge"></i><i class="badge"></i></div>
    <div class="strip"><span class="dose">2500 MG PER GUMMY</span><span class="count">30 GUMMIES</span><span class="weight">NET WT. = 4.76 OZ/(135G)</span></div>
  </section>

  <section class="label label--psy mood--defense" style="top:1212px">
    <div class="artwork" role="img" aria-label="Psychedelic mushroom landscape in black cherry red and green"></div>
    <div class="mood-copy"><div class="mood-title">IMMUNITY &amp; GUT HEALTH</div><p class="mood-ingredients">VIT A, VIT C, GINGER, MAGNESIUM GLYCINATE, LEMON BALM, MAITAKE, TURKEY TAIL, HUMULENE.</p></div>
    <div class="center"><div class="brand">Fennick Grove</div><div class="product">MUSHROOM<br>GUMMIES</div><div class="species">Amanita Muscaria</div><div class="mood-word">DEFENSE</div><div class="flavor">BLACK CHERRY</div><div class="front-ingredients">Turkey Tail</div></div>
    <div class="badges"><i class="badge"></i><i class="badge"></i><i class="badge"></i><i class="badge"></i><i class="badge"></i><i class="badge"></i><i class="badge"></i></div>
    <div class="strip"><span class="dose">2500 MG PER GUMMY</span><span class="count">30 GUMMIES</span><span class="weight">NET WT. = 4.76 OZ/(135G)</span></div>
  </section>

  <section class="label label--psy mood--focus" style="top:1594px">
    <div class="artwork" role="img" aria-label="Psychedelic mushroom landscape in peach and magenta"></div>
    <div class="mood-copy"><div class="mood-title">FOCUSED, CREATIVE,<br>PRODUCTIVE</div><p class="mood-ingredients">RHODIOLA ROSEA, THEACRINE, LUTEOLIN, FORSKOLIN, LIONS MANE, CORDYCEPS, CARYPHYLLENE, LINALOOL.</p></div>
    <div class="center"><div class="brand">Fennick Grove</div><div class="product">MUSHROOM<br>GUMMIES</div><div class="species">Amanita Muscaria</div><div class="mood-word">FOCUS</div><div class="flavor">SUNNY PLUME</div><div class="front-ingredients">Lion's Mane &amp; Cordyceps</div></div>
    <div class="badges"><i class="badge"></i><i class="badge"></i><i class="badge"></i><i class="badge"></i><i class="badge"></i><i class="badge"></i><i class="badge"></i></div>
    <div class="strip"><span class="dose">2500 MG PER GUMMY</span><span class="count">30 GUMMIES</span><span class="weight">NET WT. = 4.76 OZ/(135G)</span></div>
  </section>

  <section class="label label--psy mood--uplift" style="top:1986px">
    <div class="artwork" role="img" aria-label="Psychedelic mushroom landscape in pineapple yellow and magenta"></div>
    <div class="mood-copy"><div class="mood-title">MOOD ENHANCEMENT,<br>MENTAL HEALTH HELPER</div><p class="mood-ingredients">INGREDIENTS: MAGNESIUM, VITAMIN B2, THEACRINE, RHODIOLA ROSEA, SHIITAKE, CORDYCEPS, MYRCENE, PINENE.</p></div>
    <div class="center"><div class="brand">Fennick Grove</div><div class="product">MUSHROOM<br>GUMMIES</div><div class="species">Amanita Muscaria</div><div class="mood-word">UPLIFTING</div><div class="flavor">PINEAPPLE</div></div>
    <div class="badges"><i class="badge"></i><i class="badge"></i><i class="badge"></i><i class="badge"></i><i class="badge"></i><i class="badge"></i><i class="badge"></i></div>
    <div class="strip"><span class="dose">2500 MG PER GUMMY</span><span class="count">30 GUMMIES</span><span class="weight">NET WT. = 4.76 OZ/(135G)</span></div>
  </section>

</main>
</body>
</html>
```